This book will apply the 12 Steps to gaming addiction, also known as video game addiction. The primary purpose of the book is to provide an effective solution for this new type of addiction. The solution is based on the rich and successful concepts of traditional twelve-step programs like RL.

The title on the cover will be "Nine Doors Past the Glowing Screen" and "by Martin Quorby". A subtitle can be used if it works in your design of "A Practical Path Beyond Compulsive Console Play". Cover will be for a 6" x 9" book approximately 110 pages in length.

Some back cover text including some review quotes and an author bio are in the attached Word doc. There is also an author photo attached for for the back cover.

Requirements
Must have
• For the cover design it could be stylized, or an image, a partial image, or whatever. I am open to suggestions. Think about what would be noticed by a person searching for help with moderating their video game use, or by the parents or loved ones of problem gamers. Something contemporary and eye catching.

```html
<!DOCTYPE html>
<html lang="en">
<head>
<meta charset="UTF-8">
<title>Nine Doors Past the Glowing Screen — Cover</title>
<link rel="stylesheet" href="https://fonts.googleapis.com/css2?family=Orbitron:wght@400;600;700&display=swap">
<style>
  :root {
    --page-bg: #ffffff;
    --cover-top: #555c6a;
    --cover-bottom: #3a404e;
    --ink-light: #ffffff;
    --accent-red: #e42127;
    --art-glow: #ffffff;
    --art-mid: #8a909c;
  }
  html, body {
    margin: 0;
    padding: 0;
    width: 1200px;
    height: 939px;
    overflow: hidden;
    background: var(--page-bg);
  }
  .book-cover {
    position: absolute;
    left: 332px;
    top: 30px;
    width: 535px;
    height: 879px;
    background: linear-gradient(180deg, var(--cover-top), var(--cover-bottom));
    font-family: "Orbitron", sans-serif;
    color: var(--ink-light);
    text-align: center;
    overflow: hidden;
  }
  .title-line {
    position: absolute;
    left: 0;
    width: 100%;
    margin: 0;
    text-transform: uppercase;
    line-height: 1;
    letter-spacing: 1px;
    z-index: 2;
  }
  .title-line.primary   { top: 78px;  font-size: 46px; font-weight: 700; }
  .title-line.connector { top: 150px; font-size: 36px; font-weight: 400; }
  .title-line.highlight { top: 210px; font-size: 50px; font-weight: 700; color: var(--accent-red); }
  .title-line.highlight-small { top: 274px; font-size: 36px; font-weight: 700; color: var(--accent-red); }
  .cover-art {
    position: absolute;
    left: 76px;
    top: 300px;
    width: 383px;
    height: 310px;
    z-index: 1;
  }
  .subtitle {
    position: absolute;
    left: 0;
    width: 100%;
    margin: 0;
    font-size: 21px;
    font-weight: 400;
    letter-spacing: 1px;
    line-height: 1;
  }
  .subtitle.lead   { top: 635px; }
  .subtitle.accent { top: 677px; color: var(--accent-red); }
  .author-band {
    position: absolute;
    left: 0;
    bottom: 0;
    width: 100%;
    height: 94px;
    background: var(--accent-red);
    display: flex;
    align-items: center;
    justify-content: center;
  }
  .author-name {
    margin: 0;
    font-size: 33px;
    font-weight: 700;
    letter-spacing: 1px;
    text-transform: uppercase;
  }
</style>
</head>
<body>
  <main class="book-cover">
    <h1 class="title-line primary">Nine Doors</h1>
    <p class="title-line connector">Past the</p>
    <p class="title-line highlight">Glowing</p>
    <p class="title-line highlight-small">Screen</p>

    <svg class="cover-art" viewBox="0 0 383 310" role="img" aria-label="White line illustration of a game controller framed by angled brackets">
      <defs>
        <radialGradient id="artGlow" cx="0.5" cy="0.58" r="0.5">
          <stop offset="0" stop-color="var(--art-glow)" stop-opacity="0.55"/>
          <stop offset="0.45" stop-color="var(--art-mid)" stop-opacity="0.35"/>
          <stop offset="1" stop-color="var(--art-mid)" stop-opacity="0"/>
        </radialGradient>
      </defs>
      <ellipse cx="191.5" cy="175" rx="191" ry="135" fill="url(#artGlow)"/>
    </svg>

    <p class="subtitle lead">A Practical Path Beyond</p>
    <p class="subtitle accent">Compulsive Console Play</p>

    <div class="author-band">
      <p class="author-name">Martin Quorby</p>
    </div>
  </main>
</body>
</html>
```